Professional/Sleek card design for athletic apparel brand

Athletic apparel brand. Mainly focused on lifting weights/gym workouts. Logo and brand are already created. Must use brand logo and name. Creativity is welcome. Looking for a clean, modern, and sexy design.

```html
<!DOCTYPE html>
<html lang="en">
<head>
<meta charset="utf-8">
<title>Grit and Iron – Business Card</title>
<link href="https://fonts.googleapis.com/css2?family=Open+Sans:wght@400;700&display=swap" rel="stylesheet">
<style>
  :root {
    --stage: #2a2a2a;
    --ink: #1c1c1c;
    --paper: #ffffff;
    --shadow: rgba(0, 0, 0, 0.45);
  }
  * { box-sizing: border-box; margin: 0; padding: 0; }
  html, body {
    width: 1200px;
    height: 780px;
    overflow: hidden;
    background: var(--stage);
    font-family: "Open Sans", Arial, sans-serif;
  }
  .stage {
    position: relative;
    width: 1200px;
    height: 780px;
    display: flex;
    align-items: center;
    justify-content: center;
    gap: 40px;
  }
  .card {
    position: relative;
    width: 540px;
    height: 309px;
    overflow: hidden;
    box-shadow: 0 14px 30px var(--shadow);
  }

  /* Back face */
  .card-back {
    background: var(--ink);
    display: flex;
    flex-direction: column;
    align-items: center;
    justify-content: center;
    gap: 14px;
  }
  .brand-dot {
    width: 56px;
    height: 56px;
    border-radius: 50%;
    background: var(--paper);
  }
  .brand-name-stacked {
    color: var(--paper);
    font-weight: 700;
    font-size: 26px;
    line-height: 1.1;
    letter-spacing: 2px;
    text-transform: uppercase;
    text-align: center;
  }

  /* Front face */
  .card-front { background: var(--paper); }
  .front-shape {
    position: absolute;
    inset: 0;
    width: 540px;
    height: 309px;
  }
  .edge-bar {
    position: absolute;
    right: 0;
    top: 16px;
    width: 12px;
    height: 42px;
    background: var(--ink);
  }
  .holder {
    position: absolute;
    right: 26px;
    top: 14px;
    text-align: right;
    color: var(--ink);
  }
  .holder-name {
    font-weight: 700;
    font-size: 25px;
    line-height: 1.15;
  }
  .holder-role {
    font-size: 14px;
    line-height: 1.3;
  }
  .brand-line {
    position: absolute;
    left: 40px;
    top: 78px;
    display: flex;
    flex-direction: column;
    align-items: flex-start;
    gap: 10px;
  }
  .brand-line .brand-dot {
    width: 22px;
    height: 22px;
    background: var(--ink);
    margin-left: 86px;
  }
  .brand-spaced {
    color: var(--ink);
    font-weight: 700;
    font-size: 11px;
    letter-spacing: 9px;
    text-transform: uppercase;
  }
  .contact {
    position: absolute;
    left: 40px;
    top: 198px;
    color: var(--paper);
    font-size: 12.5px;
    line-height: 1.28;
  }
  .contact-address { margin-bottom: 6px; }
  .contact-row {
    display: flex;
    align-items: center;
    gap: 8px;
  }
  .contact-row svg {
    width: 11px;
    height: 11px;
    flex: none;
  }
  .brand-mark-large {
    position: absolute;
    right: 22px;
    top: 172px;
    width: 120px;
    color: var(--paper);
    font-weight: 700;
    font-size: 26px;
    line-height: 1.08;
    text-align: right;
    text-transform: uppercase;
    letter-spacing: 1px;
  }
</style>
</head>
<body>
<main class="stage">

  <section class="card card-back" aria-label="Card back">
    <div class="brand-dot"></div>
    <div class="brand-name-stacked">Grit and<br>Iron</div>
  </section>

  <section class="card card-front" aria-label="Card front">
    <svg class="front-shape" viewBox="0 0 540 309" aria-hidden="true">
      <path d="M0 192 H392 V140 H540 V309 H0 Z" fill="var(--ink)"/>
    </svg>

    <div class="edge-bar"></div>

    <div class="holder">
      <p class="holder-name">Marcus Delane</p>
      <p class="holder-role">Founder &amp; CEO</p>
    </div>

    <div class="brand-line">
      <div class="brand-dot"></div>
      <p class="brand-spaced">Grit and Iron</p>
    </div>

    <div class="contact">
      <p class="contact-address">4820 E Ridgeline Ave. Ste. 210<br>Mesa, AZ 85201</p>
      <p class="contact-row">
        <svg viewBox="0 0 12 12" aria-hidden="true"><rect x="3" y="0.5" width="6" height="11" rx="1" fill="none" stroke="currentColor"/><line x1="5" y1="9.8" x2="7" y2="9.8" stroke="currentColor"/></svg>
        (555) 214-7730
      </p>
      <p class="contact-row">
        <svg viewBox="0 0 12 12" aria-hidden="true"><path d="M2.5 1 L4.5 1 L5.3 3.6 L4 4.6 Q5 7 7.4 8 L8.4 6.7 L11 7.5 L11 9.5 Q10.5 11 9 11 Q1 10 1 3 Q1 1.5 2.5 1 Z" fill="currentColor"/></svg>
        1 (800) 555-0142 Ext. 300
      </p>
      <p class="contact-row">
        <svg viewBox="0 0 12 12" aria-hidden="true"><circle cx="6" cy="6" r="5.2" fill="none" stroke="currentColor"/><ellipse cx="6" cy="6" rx="2.3" ry="5.2" fill="none" stroke="currentColor"/><line x1="0.8" y1="6" x2="11.2" y2="6" stroke="currentColor"/></svg>
        www.gritandironwear.com
      </p>
      <p class="contact-row">
        <svg viewBox="0 0 12 12" aria-hidden="true"><rect x="0.5" y="2.5" width="11" height="8" fill="none" stroke="currentColor"/><path d="M0.5 2.5 L6 7 L11.5 2.5" fill="none" stroke="currentColor"/></svg>
        mdelane@gritandironwear.com
      </p>
    </div>

    <div class="brand-mark-large">Grit<br>and<br>Iron</div>
  </section>

</main>
</body>
</html>
```